Personal coach needs brochure design for inspirational essay about authenticity

Overview:
I want a beautiful brochure, 11”x17” that folds to 8-1/2”x11” with 4 pages. Think of it as an oversize greeting card.
• Front cover: photograph of a dancer and title with attribution of quote (Lumafold jpeg photo attached)
• Inside spread: Copy (Helena Brisk copy attached) with some appropriate illustration, based on cover photo
• Back cover: contact information, brief descriptive copy, two small photos (jpeg photo attached; see copy for direction)
Copy for front cover title, inside spread and back cover is attached in doc titled "Helena Brisk copy"

Purpose of brochure:
I'm a personal coach and once a year I produce a 4-page illustrated inspirational essay, which invites personal reflection on living a more mindful, meaningful life. Most people I send them to collect them. Someday in the future I'd like to put a collection of these essays into a coffee table book and also create a website for the collection, which is related to the personal coaching that I do.
I have the brochures printed hard copy. I have attached a few examples from previous years. Each has a unique design related to its theme.

Concept:
This year’s essay theme, “There will only ever be one you!” is based on a quote by Helena Brisk, a famous modern dancer. The complete quote, which appears in the copy, is about being true to one’s authentic self. The essay is not about dance, but because the author of the quote was a dancer who personified this theme of being unique to self, I have selected a photo of dance for the cover.

Design Guidance:
Front cover: One possibility is to expand the background color of the Lumafold photo so the photo seems to emerge from the background. But I am open to ideas. I think the photo is artsy enough as it is, but there may be other ways to treat it (e.g. special effects) that would also work. The title should appear somewhere. Make the attribution (--Helena Brisk) in smaller type than the title.

Inside Spread: There may be ways to borrow a design motif from the cover photo to make the inside spread more visually interesting, i.e., not just straight copy. I think it may be helpful to make the font size of the quote larger than the rest of the copy, but it has to be read in sequence. Or maybe it's printed in same size as copy, but then also repeated and displayed by itself in larger type.

Back cover: If you look at some of the other examples I’ve sent, you’ll see how the back cover is typically handled. I want a reduced version of the cover to be placed near the line that says "this is the 16th in a series.." Then, there’s a jpeg photo of Helena Brisk that should be placed next to the copy description of her.

Need extra days to review

```html
<!DOCTYPE html>
<html lang="en">
<head>
<meta charset="utf-8">
<title>There Will Only Ever Be One You! – Brochure</title>
<link rel="stylesheet" href="https://fonts.googleapis.com/css2?family=Montserrat:wght@400;500;600;700&family=Yeseva+One&display=swap">
<style>
:root{
  --ink:#15121d;
  --ink-soft:#1a1724;
  --paper:#e4e4e6;
  --white:#ffffff;
  --grey-bg:#cfcfd1;
  --rule:#6d6a75;
  --rule-light:#9a98a0;
  --photo-dark:#2a2d33;
  --photo-light:#8d939b;
}
*{margin:0;padding:0;box-sizing:border-box}
html,body{width:1200px;height:2400px;overflow:hidden}
body{background:var(--grey-bg);font-family:'Montserrat',sans-serif;color:var(--white);position:relative}
.spread{position:absolute;left:44px;width:1112px;height:720px;background:var(--ink);overflow:hidden;box-shadow:0 6px 22px rgba(0,0,0,.25)}
.spread--outer{top:440px}
.spread--inner{top:1240px}
.spread > svg.art{position:absolute;left:0;top:0}
.abs{position:absolute}
.nowrap{white-space:nowrap}
.icon{width:15px;height:15px;flex:none}

/* back cover */
.contact-pill{left:33px;top:33px;background:var(--white);color:var(--ink);font-weight:600;font-size:12.5px;letter-spacing:.6px;padding:2px 9px;border-radius:4px}
.contact-list{left:33px;top:67px;display:flex;flex-direction:column;gap:8px}
.contact-line{display:flex;align-items:center;gap:8px;font-size:11.5px;letter-spacing:.4px;height:15px}
.vdivider{left:236px;top:68px;width:1px;height:65px;background:var(--rule)}
.address{left:256px;top:68px;display:flex;gap:7px;font-size:11px;line-height:13.5px;letter-spacing:.3px}
.copyright{left:278px;top:122px;font-size:11px}
.series{left:33px;top:300px;font-size:12px;line-height:16.5px;letter-spacing:.4px}
.series strong{font-size:13.5px;font-weight:600}
.rule{height:1px;background:var(--rule)}
.heading{font-size:12.5px;font-weight:600;letter-spacing:.5px}
.small-copy{font-size:9.5px;line-height:11px;letter-spacing:.1px}
.portrait-frame{left:391px;top:406px;width:133px;height:133px;border:2px solid var(--paper);border-radius:5px;padding:4px}
.portrait-frame div{width:100%;height:100%;background:linear-gradient(160deg,#5c5b58,#2b2a29);border-radius:2px}
.cover-title{left:600px;top:566px;width:470px;text-align:center;font-family:'Yeseva One',serif;font-weight:400;font-size:38px;line-height:41px;letter-spacing:.5px}
.cover-rule{left:815px;top:658px;width:40px;height:1px;background:var(--white)}
.cover-attrib{left:600px;top:671px;width:470px;text-align:center;font-size:16px;letter-spacing:1px}

/* inside spread */
.body-copy{font-size:11.6px;line-height:14.5px;letter-spacing:.35px;white-space:nowrap}
.quote{font-size:12.8px;line-height:14.5px;letter-spacing:.5px;white-space:nowrap}
.footer{display:flex;align-items:center;gap:12px;font-size:11.5px;letter-spacing:.5px}
.footer .item{display:flex;align-items:center;gap:7px}
.footer--dark{color:var(--ink)}
</style>
</head>
<body>

<!-- Outer spread: back cover + front cover -->
<section class="spread spread--outer" aria-label="Outer spread">
  <svg class="art" width="1112" height="720" viewBox="0 0 1112 720">
    <defs>
      <radialGradient id="dancerPhoto" cx="55%" cy="50%" r="60%">
        <stop offset="0" stop-color="var(--photo-light)"/>
        <stop offset="1" stop-color="var(--photo-dark)"/>
      </radialGradient>
    </defs>
    <rect x="556" width="556" height="720" fill="var(--ink-soft)"/>
    <path d="M0 200 C160 150 420 150 530 300" fill="none" stroke="var(--paper)" stroke-width="12"/>
    <path d="M0 283 C170 205 420 215 512 345" fill="none" stroke="var(--paper)" stroke-width="3"/>
    <circle cx="818" cy="215" r="314" fill="none" stroke="var(--paper)" stroke-width="11"/>
    <circle cx="818" cy="210" r="298" fill="url(#dancerPhoto)" role="img" aria-label="Photograph of a leaping dancer in a flowing dress against a misty grey backdrop"/>
  </svg>

  <div class="abs contact-pill">Contact Us</div>
  <div class="abs contact-list">
    <div class="contact-line">
      <svg class="icon" viewBox="0 0 16 16"><circle cx="8" cy="8" r="7.5" fill="var(--white)"/><circle cx="8" cy="6" r="2.3" fill="var(--ink)"/><path d="M4 12.5c.8-2.3 2.2-3.2 4-3.2s3.2.9 4 3.2" fill="var(--ink)"/></svg>
      <span><b style="font-weight:600">Nora Valenti</b>, Ph.D.</span>
    </div>
    <div class="contact-line">
      <svg class="icon" viewBox="0 0 16 16"><circle cx="8" cy="8" r="7.5" fill="var(--white)"/><path d="M5.2 4.2l1.4-.4 1 2.2-.9.7c.4 1 1.2 1.8 2.2 2.3l.7-.9 2.2 1-.4 1.4c-3.4.3-6.6-2.9-6.2-6.3z" fill="var(--ink)"/></svg>
      <b style="font-weight:600">555-014-2298</b>
    </div>
    <div class="contact-line">
      <svg class="icon" viewBox="0 0 16 16"><circle cx="8" cy="8" r="7.5" fill="var(--white)"/><rect x="4" y="5" width="8" height="6" rx="1" fill="var(--ink)"/><path d="M4.5 5.5L8 8.3l3.5-2.8" stroke="var(--white)" stroke-width=".9" fill="none"/></svg>
      <span>nvalenti@mailbox.example</span>
    </div>
  </div>
  <div class="abs vdivider"></div>
  <div class="abs address">
    <svg class="icon" viewBox="0 0 16 16"><circle cx="8" cy="8" r="7.5" fill="var(--white)"/><path d="M8 3.5a3 3 0 0 1 3 3c0 2.2-3 5.7-3 5.7S5 8.7 5 6.5a3 3 0 0 1 3-3z" fill="var(--ink)"/><circle cx="8" cy="6.5" r="1" fill="var(--white)"/></svg>
    <span>Heron Hill House,<br>12 Orchard Lane, Millbrook,<br>Vermont 05001</span>
  </div>
  <div class="abs copyright">©2023</div>

  <p class="abs series nowrap"><strong>There Will Only Ever Be One You</strong> is the <strong>16th</strong> in a<br>series of Labor Day essays inviting a moment of reflection<br>on living a more meaningful, more mindful life.</p>
  <div class="abs rule" style="left:33px;top:360px;width:325px"></div>

  <h2 class="abs heading" style="left:33px;top:385px">About Helena Brisk:</h2>
  <p class="abs small-copy nowrap" style="left:33px;top:411px">Born in 1894, Helena Brisk danced and taught for over 70<br>years. She is recognized as a primal artistic force of the 20th<br>century, whose influence on modernity has been compared to<br>Aurel Danek, Tomas Reyne, Ivo Maren, and Elias Crowe. Her<br>themes dealt with the lives and conflicts of ordinary people,<br>and she brought serious issues to the stage like war, poverty,<br>intolerance and the injustices of slavery and treatment of<br>Native Americans. Rebelling against conventions of the past,<br>her dancing and choreography exposed the depths of human<br>emotion through intense movements that were forceful, stark,<br>angular, jagged, and percussive – startlingly unlike the formality<br>of classical ballet, which she saw as antiquated.</p>
  <div class="abs portrait-frame"><div role="img" aria-label="Black and white photograph of Helena Brisk dancing in a long white skirt"></div></div>
  <div class="abs rule" style="left:33px;top:565px;width:491px"></div>

  <h2 class="abs heading" style="left:33px;top:588px">About Photographer Clara Whitby:</h2>
  <p class="abs small-copy nowrap" style="left:33px;top:613px">In 1935 Clara Whitby saw a performance by modern dancer and choreographer Helena Brisk.<br>Whitby was so inspired by the dance performance that she introduced herself to Brisk, &amp; the two<br>artists began an artistic collaboration that lasted more than 60 years. Whitby often photographed<br>dancers in action, to capture the emotion behind their movement. Her artistic style was in line with<br>Brisk’s philosophy of dance. This photo from the dance, “Letter to the Sea,” is one of Whitby’s<br>most famous photographs. The title of this work comes from an Adela Finch poem, which<br>inspired Brisk to create a dance performance based on Finch’s life.</p>

  <h1 class="abs cover-title">There Will Only Ever<br>Be One You!</h1>
  <div class="abs cover-rule"></div>
  <div class="abs cover-attrib">Helena Brisk</div>
</section>

<!-- Inner spread -->
<section class="spread spread--inner" aria-label="Inner spread">
  <svg class="art" width="1112" height="720" viewBox="0 0 1112 720">
    <rect width="556" height="720" fill="var(--ink)"/>
    <rect x="556" width="556" height="720" fill="var(--ink-soft)"/>
    <path d="M0 568 C80 548 160 565 240 560 C320 555 380 535 402 475 C420 420 412 355 432 305 C445 265 472 232 502 208 C512 150 528 80 545 30 L556 30 L556 720 L0 720 Z" fill="var(--paper)" role="img" aria-label="Light grey silhouette illustration of a dancer drawn from the cover photo"/>
    <path d="M556 410 C600 398 680 402 760 398 C820 394 842 380 852 330 C862 262 882 222 922 192 C962 162 1002 122 1050 115 L1080 120 L1062 150 C1080 175 1098 190 1112 195 L1112 400 C1060 428 1000 438 900 444 C800 450 700 450 620 458 C590 462 570 468 556 470 Z" fill="var(--paper)" role="img" aria-label="Light grey silhouette illustration of a leaping dancer in a flowing dress"/>
  </svg>

  <p class="abs body-copy" style="left:33px;top:73px">In the rural Ohio village where I grew up, one of the highlights of Sunday<br>morning church service -- in between congregational hymn-singing and<br>the preacher’s sermon -- was the “special selection,” a musical performance<br>by a parishioner. Typically, it was a vocalist or instrumental on piano,<br>organ or violin. One Sunday, we were surprised by an unusual<br>performance. A plump, buxom farm wife approached the pulpit,<br>puckered up her lips and unexpectedly began to whistle the hymn<br><b>“The Old Rugged Cross.”</b> As a 10-year-old, I found this hilarious as<br>I tried to choke back my wide-eyed amazement and giggles.</p>
  <p class="abs body-copy" style="left:33px;top:238px">Despite the irreverence of my pre-adolescent reaction, this<br>memory has stayed with me for decades as an iconic example<br>of the wonderment of individual differences. Of the delight<br>I find in witnessing someone express herself in sometimes<br>surprising and even courageous ways. Of the marvel of<br>beholding a person be truly authentic and uniquely original.</p>
  <p class="abs body-copy" style="left:33px;top:352px">Someone who personified the irrepressible impulse to<br>express her individuality was the early 20th century dancer<br>and choreographer Helena Brisk. A pioneer of modern<br>dance, she threw tradition overboard and was inspired to<br>dance in a way that was a radical departure from the<br>formalized style and rigidly dictated forms of classical<br>ballet. Brisk felt compelled to express the rawness<br>and emotion of human experience in her dancing --<br>not just present a form of pretty entertainment.<br>Iconoclastically brilliant, she created a new<br>language of dance, a revolutionary vocabulary<br>of movement that electrified the stage,<br>often creating a visceral response<br>in the audience.</p>

  <div class="abs rule" style="left:33px;top:640px;width:491px;background:var(--rule-light)"></div>
  <div class="abs footer footer--dark" style="left:33px;top:672px">
    <span class="item"><svg class="icon" viewBox="0 0 16 16"><circle cx="8" cy="8" r="7.5" fill="var(--ink)"/><path d="M5.2 4.2l1.4-.4 1 2.2-.9.7c.4 1 1.2 1.8 2.2 2.3l.7-.9 2.2 1-.4 1.4c-3.4.3-6.6-2.9-6.2-6.3z" fill="var(--white)"/></svg><b style="font-weight:600">555-014-2298</b></span>
    <span>|</span>
    <span class="item"><svg class="icon" viewBox="0 0 16 16"><circle cx="8" cy="8" r="7.5" fill="var(--ink)"/><rect x="4" y="5" width="8" height="6" rx="1" fill="var(--white)"/><path d="M4.5 5.5L8 8.3l3.5-2.8" stroke="var(--ink)" stroke-width=".9" fill="none"/></svg>nvalenti@mailbox.example</span>
  </div>

  <p class="abs body-copy" style="left:590px;top:28px">In her biography of Brisk, her friend and equally talented choreographer<br>Vera Lindqvist recalled that despite sensational reviews for her own innovative<br>work in the Broadway musical Prairie Song!, Lindqvist had a gnawing feeling that<br>her work was only mediocre. Lindqvist confessed her anxieties to Brisk who<br>listened quietly and then responded, <b>“There will only ever be one you!”</b><br>Continuing, she added:</p>
  <div class="abs rule" style="left:590px;top:130px;width:278px"></div>
  <p class="abs quote" style="left:590px;top:144px">“ There is a vitality, a life-force,<br>an energy, a quickening that is<br>translated through you into action.<br>And because there is only one of<br>you in all of time, this expression<br>is unique. And if you block it, the<br>world will not have it. It is not your<br>business to determine how good<br>it is nor how valuable nor how it<br>compares with other expressions.<br>It is your business to keep it yours<br>clearly and directly, to keep the<br>channel open. You have to keep<br>open and aware directly to the<br>urges that motivate you. Above<br>all else, keep the channel open! ”</p>
  <div class="abs rule" style="left:590px;top:390px;width:245px"></div>

  <p class="abs body-copy" style="left:590px;top:480px">Brisk’s wisdom reminds us that we must not hold back or judge our gifts.<br>Although there may be moments when we doubt ourselves or when we worry<br>that we’re not good enough, our job is to be fearless and to “keep the channel<br>open.”</p>
  <p class="abs body-copy" style="left:590px;top:553px">Guard the precious miracle of your own uniqueness. Find that home-sweet-home<br>feeling where you feel you are your most authentic self. There will only ever be<br>one you! And importantly, respect the differences of others. Our world would be<br>a drab, boring place if we all only whistled one tune.</p>

  <div class="abs rule" style="left:590px;top:640px;width:490px"></div>
  <div class="abs footer" style="left:590px;top:672px">
    <span class="item"><svg class="icon" viewBox="0 0 16 16"><circle cx="8" cy="8" r="7.5" fill="var(--white)"/><path d="M5.2 4.2l1.4-.4 1 2.2-.9.7c.4 1 1.2 1.8 2.2 2.3l.7-.9 2.2 1-.4 1.4c-3.4.3-6.6-2.9-6.2-6.3z" fill="var(--ink)"/></svg><b style="font-weight:600">555-014-2298</b></span>
    <span>|</span>
    <span class="item"><svg class="icon" viewBox="0 0 16 16"><circle cx="8" cy="8" r="7.5" fill="var(--white)"/><rect x="4" y="5" width="8" height="6" rx="1" fill="var(--ink)"/><path d="M4.5 5.5L8 8.3l3.5-2.8" stroke="var(--white)" stroke-width=".9" fill="none"/></svg>nvalenti@mailbox.example</span>
  </div>
</section>

</body>
</html>
```